New DermaLoom logo and packaging

We would like a new design for our new product DermaLoom, a high strength vitamin C serum which treats pigmentation. The packaging will reflect a high quality, clinical product with the logo "DermaLoom" on the front, with it's ingredients "Vitamin C, B3, B5, E and ferulic acid" the products are in two sizes 10ml and 30ml.

This is one of many products to come out in the DermaLoom range.

It would be for high end medical clinics selling premium brands, with a strong medical and clinical feel, professional and current or even futuristic in appearance.

Gold, blue, silver, White, cream are all colours that do this (without appearing cheap)

The product is not tested on animals, so would have
- "Not tested on animals".
- "12m" symbol for shelf life,
- "Made in USA"
- and ingredients list

See attached the product and existing box

Target Market(s)

Medical and aesthetic clinics

Font styles to use
Serif
Sans Serif

Colors
33a6d7
cee9f5
ffffff
fbed22
fee18a

Requirements
Must have
• High end premium brand
Nice to have
• like the idea of gold and silver lettering on cream background
Should not have
• Tacky, over complicated design

```html
<!DOCTYPE html>
<html lang="en">
<head>
<meta charset="utf-8">
<title>DermaLoom Serum Label</title>
<link href="https://fonts.googleapis.com/css2?family=Crimson+Pro:wght@600;700&display=swap" rel="stylesheet">
<style>
  :root {
    --cream: #e1dad3;
    --tile: #d3b5a8;
    --tile-edge: #d8944a;
    --rule: #d18a38;
    --gold: #a8842e;
    --gold-light: #bf9a3e;
  }
  html, body {
    margin: 0;
    padding: 0;
    overflow: hidden;
  }
  .label {
    position: relative;
    width: 1200px;
    height: 1197px;
    background: var(--cream);
    overflow: hidden;
    font-family: "Crimson Pro", "Palatino Linotype", serif;
    font-weight: 700;
    color: var(--gold);
  }
  .tile {
    position: absolute;
    width: 136px;
    height: 145px;
    background: var(--tile);
    box-sizing: border-box;
    border: 1px solid var(--tile-edge);
  }
  .tile-row-top .tile { top: 0; }
  .tile-row-bottom .tile { top: 1052px; }
  .front-rule {
    position: absolute;
    top: 173px;
    width: 3px;
    height: 808px;
    background: var(--rule);
  }
  .text {
    position: absolute;
    margin: 0;
    white-space: nowrap;
    line-height: 1;
    background: linear-gradient(180deg, var(--gold-light), var(--gold));
    -webkit-background-clip: text;
    background-clip: text;
    -webkit-text-fill-color: transparent;
  }
  .centered { transform: translateX(-50%); }
  .brand-name {
    left: 298px;
    top: 568px;
    font-size: 56px;
    font-weight: 600;
    letter-spacing: 1px;
  }
  .actives {
    left: 309px;
    top: 674px;
    font-size: 28px;
  }
  .volume {
    left: 287px;
    top: 950px;
    font-size: 27px;
  }
  .volume .divider { padding: 0 6px; font-weight: 600; }
  .ingredients-title {
    left: 663px;
    top: 60px;
    font-size: 27px;
  }
  .cruelty-free {
    left: 894px;
    top: 467px;
    font-size: 27px;
  }
  .origin {
    left: 910px;
    top: 1058px;
    font-size: 27px;
  }
  .shelf-life {
    left: 904px;
    top: 1103px;
    font-size: 27px;
  }
</style>
</head>
<body>
<div class="label">
  <div class="tile-row-top">
    <div class="tile" style="left:0"></div>
    <div class="tile" style="left:152px"></div>
    <div class="tile" style="left:308px"></div>
    <div class="tile" style="left:464px"></div>
  </div>

  <div class="front-rule" style="left:13px"></div>
  <div class="front-rule" style="left:587px"></div>

  <h1 class="text centered brand-name">DermaLoom</h1>
  <p class="text centered actives">Vitamin C, B3, B5, E and ferulic acid</p>
  <p class="text centered volume">℮ 30ml <span class="divider">|</span> 1.fl. oz</p>

  <p class="text ingredients-title">Ingridients:</p>
  <p class="text centered cruelty-free">NOT TESTED ON ANIMALS</p>
  <p class="text centered origin">MADE IN USA</p>
  <p class="text centered shelf-life">12m</p>

  <div class="tile-row-bottom">
    <div class="tile" style="left:0"></div>
    <div class="tile" style="left:152px"></div>
    <div class="tile" style="left:307px"></div>
    <div class="tile" style="left:462px"></div>
  </div>
</div>
</body>
</html>
```